Plakat-Design für eine Werbeschild für ein Geflügelhof
Zielgruppe
Wir sind ein Geflügelhof, Landhandel, Hofladen, Eier stehen seit über 100 Jahren für Hof Kranwede, artgerechte Tierhaltung und Artikelvielfalt machen uns bekannt.
Aufgabenstellung
Das Werbeschild wird auf dem Hof aufgestellt und soll den Weg zum Hof zeigen.
- die Maße vom Schild: 1,50m breit x 2,40m hoch
- Grafiken werden als .ai und .pdf benötigt
- Logo ist hochgelagen
- Foto von unserer Vorstellung ist hochgeladen
Das Schild muss 400 m RECHTS drauf gedruckt haben.
Falls es zu breit wäre, könnte das Logo ja vielleicht auch über Hof Kranwede.
Das ganze wird bei plattenwerk auf eine MetoxPan-Platte in den Druck gegeben.

```html
<!DOCTYPE html>
<html lang="de">
<head>
<meta charset="utf-8">
<title>Hof Kranwede – Einkauf auf dem Bauernhof</title>
<link href="https://fonts.googleapis.com/css2?family=Amatic+SC:wght@700&display=swap" rel="stylesheet">
<style>
  :root {
    --paper: #ebe9d2;
    --farm-green: #1c6e30;
    --signal-red: #e2234f;
    --chick-yellow: #f2c11f;
    --chick-yellow-soft: #f5d04a;
  }
  * { margin: 0; padding: 0; box-sizing: border-box; }
  html, body { width: 750px; height: 1200px; overflow: hidden; background: var(--paper); }
  .sign {
    position: relative;
    width: 750px;
    height: 1200px;
    background: var(--paper);
    font-family: "Amatic SC", "Arial Narrow", sans-serif;
    font-weight: 700;
    overflow: hidden;
  }
  .brand-dot {
    position: absolute;
    left: 46px;
    top: 37px;
    width: 118px;
    height: 118px;
    border-radius: 50%;
    background: var(--farm-green);
  }
  .brand-name {
    position: absolute;
    left: 184px;
    top: 51px;
    color: var(--farm-green);
    font-size: 90px;
    line-height: 1;
    letter-spacing: 10px;
    white-space: nowrap;
  }
  .headline {
    position: absolute;
    color: var(--farm-green);
    line-height: 1;
    white-space: nowrap;
  }
  .headline-main { left: 146px; top: 182px; font-size: 192px; letter-spacing: 4px; }
  .headline-small { left: 270px; top: 344px; font-size: 90px; letter-spacing: 1.5px; }
  .headline-farm { left: 73px; top: 413px; font-size: 194px; letter-spacing: 7px; }
  .art-skater {
    position: absolute;
    left: 605px;
    top: 205px;
    width: 145px;
    height: 214px;
    border-radius: 50% 30% 20% 40%;
    background: linear-gradient(160deg, var(--chick-yellow-soft), var(--chick-yellow) 60%, #6b2b1c);
  }
  .direction-arrow {
    position: absolute;
    left: 122px;
    top: 880px;
    width: 324px;
    height: 129px;
  }
  .art-cyclist {
    position: absolute;
    left: 0;
    top: 709px;
    width: 300px;
    height: 466px;
    border-radius: 0 45% 30% 0;
    background: linear-gradient(180deg, var(--chick-yellow-soft) 0%, var(--chick-yellow) 60%, #2d8063 85%, #7a7a7a 100%);
  }
  .distance-value {
    position: absolute;
    left: 459px;
    top: 817px;
    color: var(--signal-red);
    font-size: 163px;
    line-height: 1;
    white-space: nowrap;
    transform: scaleX(1.5);
    transform-origin: left top;
  }
  .distance-unit {
    position: absolute;
    left: 692px;
    top: 893px;
    color: var(--signal-red);
    font-size: 73px;
    line-height: 1;
  }
  .distance-side {
    position: absolute;
    left: 511px;
    top: 959px;
    color: var(--signal-red);
    font-size: 80px;
    letter-spacing: 4px;
    line-height: 1;
    white-space: nowrap;
  }
</style>
</head>
<body>
<main class="sign">
  <header>
    <span class="brand-dot"></span>
    <span class="brand-name">Hof Kranwede</span>
  </header>

  <h1>
    <span class="headline headline-main">EINKAUF</span>
    <span class="headline headline-small">AUF DEM</span>
    <span class="headline headline-farm">BAUERNHOF</span>
  </h1>

  <div class="art-skater" role="img" aria-label="Illustration: gelbes Küken auf einem Skateboard"></div>

  <svg class="direction-arrow" viewBox="0 0 324 129" aria-hidden="true">
    <path d="M0 70 C70 50 150 45 216 44 L208 4 L324 62 L218 125 L216 100 C150 100 70 104 4 112 Z" fill="var(--signal-red)"/>
  </svg>

  <div class="art-cyclist" role="img" aria-label="Illustration: gelbes Huhn mit rotem Kamm auf einem grünen Fahrrad"></div>

  <div class="distance-value">400</div>
  <div class="distance-unit">M</div>
  <div class="distance-side">RECHTS</div>
</main>
</body>
</html>
```